Daily Deals Website Needs a Landing Page (Home Page will act as the landing page)

We need a landing page for a daily deals website that will act as the home page. We have attached the wire frame and logo for reference. Open to creative ideas and suggestions as long as the main elements of the wireframe are incorporated in the design. Need a very simplistic design approach like Vorplex's search page. (www.vorplex.com) . Very clean and distinct CTA's.

Target Market(s)

Customers looking for deals on everyday use items

Font styles to use
Sans Serif

Requirements
Must have
• clean design, lots of white space and strong CTA .
Nice to have
• need a clean design overall. Strong CTA
Should not have
• Cluttered look. Too many colors, keep it simple

```html
<!DOCTYPE html>
<html lang="en">
<head>
<meta charset="utf-8">
<title>Dealvia – Daily Deals</title>
<link href="https://fonts.googleapis.com/css2?family=Ubuntu:wght@300;400;500;700&family=Kalam:wght@400&display=swap" rel="stylesheet">
<style>
:root{
  --navy:#26389a;
  --green:#6cc551;
  --green-line:#8fd37a;
  --grey:#7a7a7a;
  --grey-light:#9a9a9a;
  --orange:#f7941d;
  --star:#ffd500;
  --rule:#e6e6e6;
  --white:#ffffff;
}
*{box-sizing:border-box;margin:0;padding:0}
html,body{width:1143px;height:1200px;overflow:hidden;background:var(--white)}
body{position:relative;font-family:"Ubuntu",sans-serif;color:var(--grey)}

/* header */
.header-rule{position:absolute;top:50px;height:1px;background:var(--green-line)}
.brand{position:absolute;left:0;width:1143px;top:30px;text-align:center;font-weight:700;font-size:32px;letter-spacing:1px;color:var(--navy);line-height:38px}
.tagline{position:absolute;left:0;width:1143px;top:121px;text-align:center;font-family:"Kalam",cursive;font-weight:400;font-size:23px;color:var(--navy)}
.lead{position:absolute;left:295px;top:173px;font-size:12.5px;color:var(--green)}

/* email signup */
.signup{position:absolute;height:43px}
.signup .mail{position:absolute;left:0;top:8px;width:30px;height:28px}
.signup .field{position:absolute;left:24px;right:0;top:0;bottom:0;border:1.5px solid var(--green);border-radius:22px;background:var(--white);overflow:hidden}
.signup .field span{position:absolute;left:16px;top:0;line-height:40px;font-size:11px;font-weight:300;color:var(--grey-light)}
.signup .btn{position:absolute;right:0;top:0;bottom:0;background:var(--green);color:var(--white);font-weight:500;font-size:11.5px;display:flex;align-items:center;justify-content:center;border-radius:0 22px 22px 0}

/* nav */
.catnav{position:absolute;left:0;top:268px;width:1143px;height:25px;border-top:1px solid var(--rule);border-bottom:1px solid var(--rule)}
.catnav ul{list-style:none;position:absolute;left:149px;width:844px;top:0;display:flex;justify-content:space-between;line-height:23px;font-size:10px;font-weight:300;color:var(--navy)}

/* search */
.search{position:absolute;border:1.5px solid var(--navy);border-radius:16px;overflow:hidden;background:var(--white)}
.search svg{position:absolute;left:15px;top:50%;transform:translateY(-50%)}
.search .ph{position:absolute;left:32px;top:0;font-size:9px;font-weight:300;color:var(--grey-light)}
.search .btn{position:absolute;right:0;top:0;bottom:0;background:var(--navy);color:var(--white);font-weight:500;font-size:9.5px;display:flex;align-items:center;justify-content:center}

.section-title{position:absolute;left:0;width:1143px;text-align:center;font-weight:700;font-size:29px;color:var(--navy);letter-spacing:.3px}

/* deal cards */
.deal{position:absolute;top:440px;width:357px;height:235px;border:1px solid var(--green-line);background:var(--white)}
.deal .tag{position:absolute;left:14px;top:11px;font-size:12.5px;color:var(--green)}
.deal .name{position:absolute;left:14px;top:42px;width:180px;font-size:15px;line-height:21.5px;color:var(--grey);white-space:nowrap}
.deal .stars{position:absolute;left:14px;top:85px}
.deal .was{position:absolute;left:14px;top:108px;font-size:10px;color:var(--grey-light)}
.deal .was b{font-weight:400;font-size:18px;margin-left:3px}
.deal .now{position:absolute;left:14px;top:134px;font-size:19px;color:var(--orange)}
.deal .now b{font-weight:400;font-size:26px}
.deal .photo{position:absolute}
.deal .buy{position:absolute;left:14px;right:14px;top:186px;height:34px;border-radius:17px;background:var(--green);color:var(--white);font-weight:500;font-size:12px;letter-spacing:.4px;display:flex;align-items:center;justify-content:center}
.see-more{position:absolute;right:151px;top:700px;font-size:12.5px;color:var(--navy)}

/* footer */
.footer-rule{position:absolute;left:0;width:1143px;height:1px;background:var(--rule)}
.fcol{position:absolute;top:888px}
.fcol h4{font-weight:400;font-size:11px;color:var(--navy);letter-spacing:.3px;line-height:14px}
.fcol ul{list-style:none;margin-top:8px;font-size:9.5px;font-weight:300;color:var(--grey-light)}
.fcol li{height:21.4px;line-height:14px;display:flex;align-items:center;gap:5px}
.fcol li svg{flex:none}
.socials{position:absolute;left:714px;top:1002px;display:flex;gap:7.5px}
.socials span{width:21px;height:21px;border-radius:50%;background:var(--navy)}
.copyright{position:absolute;left:0;width:1143px;top:1153px;text-align:center;font-size:9.5px;font-weight:300;color:var(--grey-light)}
</style>
</head>
<body>

<!-- header -->
<div class="header-rule" style="left:0;width:476px"></div>
<div class="header-rule" style="left:667px;width:476px"></div>
<div class="brand">DEALVIA</div>

<h1 class="tagline">Get the best deal with Dealvia!</h1>
<p class="lead">Be the first one to hear about our best daily deals!</p>

<div class="signup" style="left:295px;top:197px;width:553px">
  <svg class="mail" viewBox="0 0 30 28"><rect x="1.5" y="1.5" width="27" height="25" fill="none" stroke="#6cc551" stroke-width="3"/><path d="M2 3 L15 15 L28 3" fill="none" stroke="#6cc551" stroke-width="3"/></svg>
  <div class="field"><span>Write your e-mail address...</span></div>
  <div class="btn" style="width:121px">SIGN UP</div>
</div>

<nav class="catnav">
  <ul>
    <li>Clothes</li><li>Shoes</li><li>Accessories</li><li>Health &amp; Beauty</li><li>Electronic Devices</li><li>Furniture</li><li>Household Appliances</li><li>Garden</li><li>Children</li><li>Pets</li>
  </ul>
</nav>

<div class="search" style="left:295px;top:308px;width:553px;height:28px">
  <svg width="10" height="10" viewBox="0 0 10 10"><circle cx="4" cy="4" r="3" fill="none" stroke="#9a9a9a" stroke-width="1.2"/><path d="M6.2 6.2 L9 9" stroke="#9a9a9a" stroke-width="1.3"/></svg>
  <span class="ph" style="line-height:25px">Search for items...</span>
  <div class="btn" style="width:120px">SEARCH</div>
</div>

<h2 class="section-title" style="top:356px">DEALS OF THE DAY</h2>

<!-- deal 1 -->
<article class="deal" style="left:173px">
  <div class="tag">Featured</div>
  <div class="name">Pressa GL200 Professional<br>Electronic Iron, Silver</div>
  <svg class="stars" width="102" height="18" viewBox="0 0 102 18">
    <defs><path id="st" d="M9 0.5 L11.3 6.4 L17.6 6.6 L12.6 10.5 L14.4 16.6 L9 13 L3.6 16.6 L5.4 10.5 L0.4 6.6 L6.7 6.4 Z"/></defs>
    <use href="#st" fill="#ffd500"/><use href="#st" x="21" fill="#ffd500"/><use href="#st" x="42" fill="#ffd500"/><use href="#st" x="63" fill="#ffd500"/><use href="#st" x="84" fill="#ffd500"/>
  </svg>
  <div class="was">Was: <b>$27.99</b></div>
  <div class="photo" role="img" aria-label="Product photo of a silver electronic steam iron" style="left:204px;top:22px;width:137px;height:145px;border-radius:6px;background:linear-gradient(135deg,#e9e9ec,#c9cacf 55%,#9c2a45)"></div>
  <div class="buy">BUY NOW</div>
</article>

<!-- deal 2 -->
<article class="deal" style="left:635px">
  <div class="tag">Promoted</div>
  <div class="name">Hollin Clothes Closet<br>Portable Wardrobe</div>
  <svg class="stars" width="102" height="18" viewBox="0 0 102 18">
    <use href="#st" fill="#ffd500"/><use href="#st" x="21" fill="#ffd500"/><use href="#st" x="42" fill="#ffd500"/><use href="#st" x="63" fill="#ffd500"/><use href="#st" x="84" fill="#ffd500"/>
  </svg>
  <div class="was">Was: <b>$69.99</b></div>
  <div class="now">Now: <b>$44.99</b></div>
  <div class="photo" role="img" aria-label="Product photo of a dark portable fabric wardrobe filled with clothes" style="left:200px;top:8px;width:143px;height:167px;background:linear-gradient(160deg,#4a4a4a,#2a2a2a 60%,#5d6b7a)"></div>
  <div class="buy">BUY NOW</div>
</article>

<a class="see-more">See more...</a>

<h2 class="section-title" style="top:732px">SUBSCRIBE</h2>

<div class="signup" style="left:293px;top:790px;width:553px">
  <svg class="mail" viewBox="0 0 30 28"><rect x="1.5" y="1.5" width="27" height="25" fill="none" stroke="#6cc551" stroke-width="3"/><path d="M2 3 L15 15 L28 3" fill="none" stroke="#6cc551" stroke-width="3"/></svg>
  <div class="field"><span>Write your e-mail address...</span></div>
  <div class="btn" style="width:121px">SIGN UP</div>
</div>

<!-- footer -->
<div class="footer-rule" style="top:862px"></div>

<div class="fcol" style="left:150px">
  <h4>CATEGORIES</h4>
  <ul>
    <li>Clothes</li><li>Shoes</li><li>Accessories</li><li>Health &amp; Beauty</li><li>Electronic Devices</li><li>Furniture</li><li>Household Appliances</li><li>Garden</li><li>Children</li><li>Pets</li>
  </ul>
</div>

<div class="fcol" style="left:338px">
  <h4>SEARCH</h4>
</div>
<div class="search" style="left:338px;top:913px;width:286px;height:29px">
  <svg width="8" height="8" viewBox="0 0 10 10"><circle cx="4" cy="4" r="3" fill="none" stroke="#9a9a9a" stroke-width="1.3"/><path d="M6.2 6.2 L9 9" stroke="#9a9a9a" stroke-width="1.4"/></svg>
  <span class="ph" style="left:29px;line-height:26px">Search for items...</span>
  <div class="btn" style="width:78px">SEARCH</div>
</div>
<div class="fcol" style="left:338px;top:967px"><h4 style="color:var(--green)">SUBSCRIBE</h4></div>
<div class="signup" style="left:314px;top:992px;width:310px;height:29px">
  <div class="field" style="border-radius:15px"><span style="line-height:26px;font-size:9.5px;left:14px">Write your e-mail address...</span></div>
  <div class="btn" style="width:78px;font-size:9.5px;border-radius:0 15px 15px 0">SIGN UP</div>
</div>

<div class="fcol" style="left:713px">
  <h4>STAY CONNECTED</h4>
  <ul>
    <li><svg width="10" height="10" viewBox="0 0 10 10"><path d="M2 1 L4 1 L4.8 3.2 L3.6 4.2 Q4.6 6 6 6.6 L7 5.4 L9 6.2 L9 8.4 Q9 9.3 8 9.2 Q2.5 8.6 1 2.2 Q0.9 1 2 1 Z" fill="none" stroke="#26389a" stroke-width="1"/></svg>XXX-XXX-XXX</li>
    <li><svg width="11" height="9" viewBox="0 0 11 9"><rect x=".6" y=".6" width="9.8" height="7.8" fill="none" stroke="#26389a" stroke-width="1"/><path d="M.8 1 L5.5 5 L10.2 1" fill="none" stroke="#26389a" stroke-width="1"/></svg>dealvia@email.com</li>
    <li><svg width="11" height="10" viewBox="0 0 11 10"><path d="M1 5 L5.5 1 L10 5 M2.5 4 L2.5 9.3 L8.5 9.3 L8.5 4 M4.5 9.3 L4.5 6.5 L6.5 6.5 L6.5 9.3" fill="none" stroke="#26389a" stroke-width="1"/></svg>Address Line 1</li>
    <li style="padding-left:16px">Address Line 2</li>
  </ul>
</div>
<div class="socials"><span></span><span></span><span></span></div>

<div class="fcol" style="left:905px">
  <h4>MORE</h4>
  <ul>
    <li>About Dealvia</li><li>Customer Support</li><li>Refund Policy</li><li>Terms &amp; Conditions</li><li>Privacy Policy</li>
  </ul>
</div>

<div class="footer-rule" style="top:1142px"></div>
<div class="copyright">Copyright ©Dealvia 2021</div>

</body>
</html>
```